Property maintenance company needs an eye catching postcard design

We are a property maintenance company that wants to send out a postcard targeting residential homeowners only. We want the postcard to create the impression of a friendly and inviting company that makes maintenance easy for homeowners. I have attached all the instructions in a pdf file as well as any other needed pictures or info. Please read the outline I provided. I also attached pictures/screenshots of our new (in progress) website if you wish to get a feel for our company.

Thanks!

Target Market(s)

residential homeowners, homeowners

Industry/Entity Type

Property Maintenance

```html
<!DOCTYPE html>
<html lang="en">
<head>
<meta charset="UTF-8">
<title>TrueHaven Maintenance Services – Postcard</title>
<link href="https://fonts.googleapis.com/css2?family=Montserrat:wght@400;500;600;700;800;900&family=Roboto+Condensed:wght@400;500&display=swap" rel="stylesheet">
<style>
  :root{
    --backdrop:#e4e4e4;
    --navy:#13288a;
    --blue:#2a5bd7;
    --pill:#3a6ae8;
    --green:#74c43f;
    --green-dark:#4ea622;
    --white:#ffffff;
    --ink:#111111;
  }
  *{box-sizing:border-box;margin:0;padding:0}
  html,body{width:1200px;height:1200px;overflow:hidden;background:var(--backdrop)}
  body{position:relative;font-family:"Montserrat",sans-serif}

  .card{position:absolute;width:766px;height:510px;background:var(--white);overflow:hidden}
  .card--front{left:69px;top:46px}
  .card--back{left:342px;top:606px}
  .layer{position:absolute}

  /* FRONT */
  .house-photo{left:0;top:0;width:500px;height:350px;
    background:linear-gradient(180deg,#dfe8f0 0%,#c9d2d6 22%,#8c8f88 50%,#6f7866 68%,#5f8a3a 100%);
    -webkit-mask-image:linear-gradient(90deg,#000 65%,transparent 100%);
    mask-image:linear-gradient(90deg,#000 65%,transparent 100%)}
  .front-waves{left:0;top:0;width:766px;height:510px}
  .service-photo{position:absolute;border-radius:50%;border:5px solid var(--green)}
  .service-photo--plumbing{left:27px;top:299px;width:128px;height:128px;background:radial-gradient(circle at 40% 40%,#f4f4f2,#c9cacb 60%,#8c8f94)}
  .service-photo--carpentry{left:164px;top:324px;width:128px;height:128px;background:radial-gradient(circle at 50% 40%,#dfe6ea,#b08a64 60%,#7a5636)}
  .service-photo--electrical{left:302px;top:290px;width:128px;height:128px;background:radial-gradient(circle at 50% 50%,#e7c6b1,#c9a38c 50%,#8a6e60)}

  .brand{position:absolute;color:var(--navy);font-weight:700;letter-spacing:.5px;line-height:1}
  .brand-sub{position:absolute;color:var(--blue);font-weight:600;font-size:10px;letter-spacing:6.2px;line-height:1}
  .card--front .brand{left:462px;top:92px;font-size:36px}
  .card--front .brand-sub{left:437px;top:138px}

  .headline{position:absolute;left:420px;top:168px;width:320px;text-align:center}
  .headline-main{display:block;color:var(--navy);font-weight:800;font-size:25px;line-height:1}
  .headline-sub{display:block;color:var(--green);font-weight:600;font-size:21.5px;line-height:1;margin-top:3px}

  .promise-pill{position:absolute;left:409px;top:233px;width:334px;height:40px;border-radius:8px;background:var(--pill);
    color:var(--white);font-weight:700;font-size:14px;line-height:15px;text-align:center;padding-top:5px;
    box-shadow:0 4px 6px rgba(0,0,0,.25)}

  .divider{position:absolute;left:458px;top:391px;width:2px;height:101px;background:var(--white)}
  .pitch{position:absolute;left:472px;top:393px;color:var(--white);font-weight:500;font-size:17px;line-height:19px;letter-spacing:.2px}
  .pitch-answer{position:absolute;left:472px;top:471px;color:var(--green);font-weight:900;font-size:18.5px;line-height:1}

  .contact-item{position:absolute;top:466px;display:flex;align-items:center;gap:7px;color:var(--white);
    font-family:"Roboto Condensed",sans-serif;font-size:24px;line-height:1;white-space:nowrap}
  .contact-item svg{width:17px;height:17px;flex:none}
  .contact-item--phone{left:17px}
  .contact-item--web{left:190px;letter-spacing:-.6px}

  /* BACK */
  .worker-photo{left:0;top:0;width:520px;height:252px;background:linear-gradient(100deg,#1c3386 0%,#243d95 50%,#2f4c9e 100%)}
  .home-photo{left:0;top:253px;width:520px;height:122px;background:linear-gradient(180deg,#b7cfe6 0%,#c5cdd2 45%,#9fae82 80%,#6f9b4a 100%)}
  .tools-photo{left:330px;top:253px;width:190px;height:122px;background:radial-gradient(ellipse at 60% 55%,#d9a43a,#6a5b4a 55%,transparent 80%)}
  .contact-band{left:0;top:378px;width:520px;height:132px;background:var(--green)}
  .back-curve{left:0;top:0;width:766px;height:510px}

  .offer-title{position:absolute;left:33px;top:28px;color:var(--white);font-weight:800;font-size:22px;letter-spacing:.5px;line-height:1}
  .offer-rule{position:absolute;left:33px;top:56px;width:45px;height:2px;background:var(--green)}
  .offer-list{position:absolute;left:31px;top:67px;list-style:none;color:var(--white);font-weight:500;font-size:16.5px;line-height:21.5px}
  .offer-list li{display:flex;align-items:center;gap:5px}
  .offer-list svg{width:13px;height:13px}

  .trade{position:absolute;top:160px;width:80px;text-align:center}
  .trade-badge{width:58px;height:58px;margin:0 auto;border-radius:50%;background:radial-gradient(circle at 40% 35%,#ffffff,#d4d6d8 80%);
    border:2px solid #b9bdc2;display:flex;align-items:center;justify-content:center}
  .trade-badge svg{width:32px;height:32px}
  .trade-label{display:block;margin-top:12px;color:var(--green);font-weight:600;font-size:8.5px;letter-spacing:.2px}
  .trade-more{position:absolute;left:437px;top:219px;color:var(--green);font-weight:500;font-size:11px;line-height:10px}

  .big-phone{position:absolute;left:36px;top:386px;display:flex;align-items:center;gap:6px;color:var(--navy);font-weight:800;font-size:41px;line-height:1}
  .big-phone svg{width:30px;height:30px}
  .big-web{position:absolute;left:41px;top:428px;color:var(--navy);font-weight:600;font-size:23px;letter-spacing:.4px;line-height:1}
  .accredit-badge{position:absolute;left:158px;top:459px;width:89px;height:34px;border-radius:4px;background:#1d4f86;border:2px solid #ffffff}
  .accredit-badge::before{content:"";position:absolute;left:3px;top:3px;width:24px;height:24px;border-radius:2px;background:var(--white)}

  .stamp-box{position:absolute;left:677px;top:26px;width:61px;height:61px;border:1.5px solid var(--ink)}
  .card--back .brand{left:494px;top:432px;font-size:31px}
  .card--back .brand-sub{left:481px;top:471px;font-size:9.5px;letter-spacing:5.4px}
</style>
</head>
<body>

<section class="card card--front" aria-label="Postcard front">
  <div class="layer house-photo" role="img" aria-label="Photo of a large two-storey suburban home with a manicured front lawn"></div>
  <svg class="layer front-waves" viewBox="0 0 766 510" aria-hidden="true">
    <path d="M0,300 C120,352 250,382 420,345 C570,300 680,300 766,410 L766,510 L0,510 Z" fill="var(--green)"/>
    <path d="M0,330 C150,382 280,402 430,372 C575,336 670,348 766,455 L766,510 L0,510 Z" fill="var(--blue)"/>
  </svg>
  <div class="service-photo service-photo--plumbing" role="img" aria-label="Photo of a hand tightening a sink pipe with a wrench"></div>
  <div class="service-photo service-photo--carpentry" role="img" aria-label="Photo of a carpenter hammering on wooden boards"></div>
  <div class="service-photo service-photo--electrical" role="img" aria-label="Photo of hands wiring an electrical outlet"></div>

  <div class="brand">TRUEHAVEN</div>
  <div class="brand-sub">MAINTENANCE SERVICES</div>

  <h1 class="headline">
    <span class="headline-main">TRUEHAVEN MAKES</span>
    <span class="headline-sub">HOME MAINTENANCE EASY</span>
  </h1>
  <div class="promise-pill">ONE POINT OF CONTACT FOR ALL YOUR<br>PROPERTY MAINTENANCE NEEDS</div>

  <div class="divider"></div>
  <p class="pitch">TIRED OF FINDING,<br>COMPARING AND<br>EVALUATING MULTIPLE<br>SERVICE PROVIDERS?</p>
  <p class="pitch-answer">WE HAVE THE SOLUTION!</p>

  <div class="contact-item contact-item--phone">
    <svg viewBox="0 0 24 24" fill="var(--green)"><path d="M6.6 10.8a15 15 0 0 0 6.6 6.6l2.2-2.2a1 1 0 0 1 1-.25 11 11 0 0 0 3.6.6 1 1 0 0 1 1 1V20a1 1 0 0 1-1 1A17 17 0 0 1 3 4a1 1 0 0 1 1-1h3.5a1 1 0 0 1 1 1c0 1.25.2 2.45.6 3.6a1 1 0 0 1-.25 1z"/></svg>
    <span>555-014-2290</span>
  </div>
  <div class="contact-item contact-item--web">
    <svg viewBox="0 0 24 24" fill="none" stroke="var(--green)" stroke-width="1.8"><circle cx="12" cy="12" r="9.5"/><ellipse cx="12" cy="12" rx="4.5" ry="9.5"/><path d="M2.5 12h19M4 7h16M4 17h16"/></svg>
    <span>www.truehavenhome.com</span>
  </div>
</section>

<section class="card card--back" aria-label="Postcard back">
  <div class="layer worker-photo" role="img" aria-label="Blue-toned photo of a construction worker in a hard hat working on lumber"></div>
  <div class="layer home-photo" role="img" aria-label="Soft-focus photo of a suburban house"></div>
  <div class="layer tools-photo" role="img" aria-label="Photo of a tool belt with gloves, hammer and screwdrivers"></div>
  <div class="layer contact-band"></div>
  <svg class="layer back-curve" viewBox="0 0 766 510" aria-hidden="true">
    <path d="M458,0 C545,120 525,330 372,510 L766,510 L766,0 Z" fill="var(--white)"/>
    <path d="M458,0 C545,120 525,330 372,510" fill="none" stroke="var(--green-dark)" stroke-width="7"/>
  </svg>

  <h2 class="offer-title">WHAT WE OFFER:</h2>
  <div class="offer-rule"></div>
  <ul class="offer-list">
    <li><svg viewBox="0 0 16 16" fill="none" stroke="var(--green)" stroke-width="1.5"><circle cx="8" cy="8" r="7"/><path d="M4.5 8.2l2.3 2.3 4.7-4.8"/></svg>Maintenance Packages</li>
    <li><svg viewBox="0 0 16 16" fill="none" stroke="var(--green)" stroke-width="1.5"><circle cx="8" cy="8" r="7"/><path d="M4.5 8.2l2.3 2.3 4.7-4.8"/></svg>Handyman Repairs</li>
    <li><svg viewBox="0 0 16 16" fill="none" stroke="var(--green)" stroke-width="1.5"><circle cx="8" cy="8" r="7"/><path d="M4.5 8.2l2.3 2.3 4.7-4.8"/></svg>Home Renovations</li>
  </ul>

  <div class="trade" style="left:16px">
    <div class="trade-badge"><svg viewBox="0 0 32 32" fill="none" stroke="var(--green)" stroke-width="2.4"><circle cx="16" cy="16" r="12"/><rect x="12" y="12" width="9" height="8" rx="2"/><path d="M21 14h4M21 18h4M12 16H8"/></svg></div>
    <span class="trade-label">ELECTRICAL</span>
  </div>
  <div class="trade" style="left:84px">
    <div class="trade-badge"><svg viewBox="0 0 32 32" fill="var(--green)"><circle cx="16" cy="15" r="7"/><rect x="4" y="19" width="24" height="6"/></svg></div>
    <span class="trade-label">MILLWORK</span>
  </div>
  <div class="trade" style="left:152px">
    <div class="trade-badge"><svg viewBox="0 0 32 32" fill="var(--green)"><rect x="5" y="22" width="22" height="4"/><rect x="5" y="17" width="14" height="3"/><path d="M16 5l2-2 8 8-2 2z"/><rect x="17" y="9" width="2" height="10" transform="rotate(-45 18 14)"/></svg></div>
    <span class="trade-label">FLOORING</span>
  </div>
  <div class="trade" style="left:221px">
    <div class="trade-badge"><svg viewBox="0 0 32 32" fill="none" stroke="var(--green)" stroke-width="3.5" stroke-linecap="round"><path d="M7 7l18 18M25 7L7 25"/></svg></div>
    <span class="trade-label">CARPENTRY</span>
  </div>
  <div class="trade" style="left:290px">
    <div class="trade-badge"><svg viewBox="0 0 32 32" fill="var(--green)"><rect x="7" y="5" width="4" height="22"/><path d="M11 10h10a5 5 0 0 1 5 5v3h-4v-3a1 1 0 0 0-1-1H11z"/><circle cx="24" cy="23" r="2"/></svg></div>
    <span class="trade-label">PLUMBING</span>
  </div>
  <div class="trade" style="left:359px">
    <div class="trade-badge"><svg viewBox="0 0 32 32" fill="var(--green)"><rect x="6" y="5" width="20" height="7" rx="1"/><path d="M26 8h2v7H17v4h-2v-6h11z"/><rect x="14" y="19" width="4" height="9" rx="1"/></svg></div>
    <span class="trade-label">PAINTING</span>
  </div>
  <div class="trade-more">and<br>more.</div>

  <div class="big-phone">
    <svg viewBox="0 0 24 24" fill="var(--navy)"><path d="M6.6 10.8a15 15 0 0 0 6.6 6.6l2.2-2.2a1 1 0 0 1 1-.25 11 11 0 0 0 3.6.6 1 1 0 0 1 1 1V20a1 1 0 0 1-1 1A17 17 0 0 1 3 4a1 1 0 0 1 1-1h3.5a1 1 0 0 1 1 1c0 1.25.2 2.45.6 3.6a1 1 0 0 1-.25 1z"/></svg>
    <span>555-014-7731</span>
  </div>
  <div class="big-web">www.truehavenhome.com</div>
  <div class="accredit-badge" aria-hidden="true"></div>

  <div class="stamp-box"></div>
  <div class="brand">TRUEHAVEN</div>
  <div class="brand-sub">MAINTENANCE SERVICES</div>
</section>

</body>
</html>
```